RESTAURANT MENU

WANTING TO CHANGE MENU DESIGN AND ADD SOME PLATES AND DESSERTS

ILL POST PICTURES OF LOGO AND PLATES. DONT HAVE ANYTHING IN MIND JUST NEED SOMETHING NEW THAT WILL STAND OUT .

Industry/Entity Type

Restaurant

Requirements
Must have
• THE SIZE RIGHT NOW IS 11X17 TRIFOLD MENU.
• IF ITS TOO CROWDED WITH THE NEW PLATES I DONT MIND MAKING IT BIGGER .
• ADD ONS
• ******************************** PASTAS **************************
• CHICKEN FETTUCCINE OR PENNE PASTA - 9.25
• SHRIMP FETTUCCINE OR PENNE PAST 10.25
• ******************* WINGS ***************************************
• BONELESS OR TRADITIONAL
• 5 WINGS - 5.99
• 10 WINGS - 8.99
• 20 WINGS - 14.99
• 50 WINGS - 35.99
• mild , hot , lemon pepper , sweet chili , teriyaki , garlic Parmesan
• *****************FROM THE BAR-B-QUE*************
• BABY BACK RIBS
• half rack - 12.99
• full rack - 18.99
• BRISKET BURGER 8.25
• BARBECUE COMBO - 17.99
• half rack of ribs, brisket , and sausage
• served with potato salad and red beans.
Should not have
• ADRESS CORRECTION ****
• 718 N. CALLOWAY ST.
• ELSA TEXAS
• ************* APPETIZERS***********
• Jalapeno cheese fries ............................. 4.99
• Mozzarella cheese sticks ........................ 5.25
• Classic Nachos ( ground bee) ................. 6.99
• Nachos ( fajita or chicken fajita ).............. 7.99
• Panchos ....................................................8.99
• ( includes lettuce , and avocado )
• Shrimp Nachos ........................................8.99
• Choriqueso...............................................6.99
• Guacamole ..............................................5.99
• ***************SALADS******************
• House Salad ...........................................5.99
• Caesar Salad...........................................5.99
• Chef Salad ...............................................7.99
• Grilled or Crispy chicken Salad ................8.99
• Shrimp Salad ............................................9.99
• ***************BURGERS AND SANDWICHES ****************
• Fajita Steak Burger .............................................................8.95
• (fine cut fajita loaded with fresh sauteed mushrooms , and topped with
• mozzarella cheese, crisp lettuce , onions , tomatoes mayo & mustard)
• Mushroom Swiss Burger .....................................................8.95
• (loaded with fresh saureed mushrooms, and topped with melted Swiss cheese)
• Hawaiian Burger ..................................................................7.99
• (topped with pineapple , american cheese , crisp lettuce , tomatoes and mayo. )
• Barbecue Burger.......................................................................7.99
• (basted with our original Bbq sauce, American cheese , lettuce , fresh tomatoes , mayo and mustard.)
• Patty Melt ................................................................................7.99
• Cheese Burger ........................................................................6.99
• Double Cheese Burger............................................................7.99
• Grilled or Fried Chicken Burger ................................................6.99
• Fish Burger ..............................................................................6.99
• (breaded fish with lettuce, tomatoes & tartar sauce )
• Blt..................................................................................4.99
• (bacon , lettuce & tomato sandwich )
• *******all burgers are served with french fries ***************
• *******ADD THREE SLICES OF BACON TO ANY BURGER ******
• ..................................1.25.
• **************KIDS MENU *****************
• Hamburger combo ..................................3.50
• cheese burger combo ..............................3.99
• Grilled ham and cheese ...........................3.50
• Chicken Tenders .......................................3.99
• Enchilada plate .........................................3.99
• (two enchiladas , rice & beans )
• Ground Beef tacos ...................................3.99
• (2 crispy or soft ground beef tacos , lettuce and cheese )
• ***************SPECIALTIES ***********************
• Chile Relleno ......................................................9.99
• (ground beef or cheese )
• Shrimp and cheese Chile Relleno ......................10.99
• Hamburger steak .................................................8.99
• 8 oz Grilled Chicken Breast .................................8.99
• Chicken Fried Chicken ........................................8.99
• Chicken Fried Steak .............................................8.99
• T Bone .................................................................12.99
• Pork Chops ..........................................................8.99
• Arrachera Steak ...................................................9.99
• ****************COMBINATION PLATES***********************
• Lurma's Special ..................................................8.99
• (fajita with two enchiladas on the side , rice and beans )
• Tampiquena .........................................................9.99
• (fajita steak with two enchiladas on the side , rice and beans
• Rio Bravo Plate .....................................................11.99
• (1 beef or cheese chile relleno with fajita steak on the side , rice and beans )
• Fajita & Shrimp plate .............................................11.99
• T Bone & Shrimp ......................................................13.99
• ************SOUTH OF THE BORDER ****************
• Cheese Enchiladaas ..................................................7.99
• Beef or Chicken Enchiladas ......................................8.99
• Mexican Plate .............................................................9.50
• (three enchiladas , one ground beef taco, and one chicken chalupa )
• Bean and Cheese Chalupa...........................................7.99
• Beef or Chicken Chalupas............................................8.99
• Chicken Flautas ..........................................................8.99
• Beef Milanesa .............................................................8.99
• Chicken Milanesa..........................................................8.99
• Bisteck Ranchero ..........................................................8.99
• Fajita or Chicken plate ...................................................8.99
• Fajita Toreada ................................................................8.99
• Pechuga Santa Fe.........................................................8.99
• Carne Guisada Plate......................................................8.99
• Fajita or Chicken Quesadillas .......................................9.99
• Shrimp Quesadillas ......................................................10.99
• Fajita or Chicken Tacos .................................................8.99
• Ground Beef tacos ( crispy or soft )...............................7.99
• **all Plates are served with rice and beans ***
• ****************TACOS ************
• Chicken fajita taco .....................................2.99
• Fajita taco ..................................................2.99
• Carne guisada ..........................................2.99
• Ground Beef taco ......................................2.50
• ************SOUPS ******************
• Caldo de Res ..........................small 6.99.................large....7.99
• Caldo de Pescado y Camaron ..small 7.99..............large ....8.99
• Caldo Siete Mares .....................small 8.99.............large ....9.99
• Menudo ....................................small ..6.99.............large ..7.99
• Caldo Tlalpeno ..........................small .. 7.99........large 8.99
• *********SEAFOOD*************
• Fish Tacos .................................................8.99
• (fish filet on corn tortilla , rice on the side )
• Fish Plate (Grilled or Fried ).........................11.99
• Shrimp Plate (any style)................................12.99
• (al mojo de ajo, ala diabla, agua chiles , fried)
• Costa Azul ....................................................14.99
• ( 6 shrimp wrapped in bacon and breaded to perfection , filled with mozzarella cheese , served with fries , rice and salad )
• Seafood Fiesta .............................................14.99
• ( combination of fish , shrimp and crab)
• Shrimp Cocktail .......................................small ..9.99.....large...12.99
• ***********FAMILY PLATTERS **************************
• Botana or Sombrero for 1 .............................................10.99
• Botana or Sombrero for 2 ..............................................20.99
• Botana or Sombrero for 3 ..............................................27.99
• Botana or Sombrero for 4 ..............................................38.99
• Botana or Sombrero for 6................................................49.99
• (beef chicken or mixed )
• Seafood platter for 2 ........................................................25.99
• Seafood platter for 3 ........................................................33.99
• Seafood platter for 4 ........................................................44.99
• Seafood platter for 6.........................................................59.99
• Mar y Tierra for 2 ............................................................26.99
• Mar y Tierra for 3 ............................................................35.99
• Mar y Tierra for 4 .............................................................43.99
• Mar y Tierra for 6...............................................................58.99
• *********BREAKFAST PLATES *************************
• Potato & Egg Plate ...................................4.99
• Bacon & Egg Plate ....................................4.99
• Migas & Egg Plate.....................................4.99
• Huevos Rancheros ...................................4.99
• Huevo ala Mexicana ..................................4.99
• Chorizo & Egg Plate ..................................4.99
• Sausage & Egg Plate ................................4.99
• Ham & Egg Plate........................................4.99
• Machacado & Egg Plate ............................5.99
• Chicharron en Salsa.....................................5.99
• Chicharron & Egg Plate................................5.99
• Chicharron en salsa with 2 eggs ..................6.99
• Chilaquiles .................................................5.99
• Huevos Divorciados ...................................6.99
• Chicken Chilaquiles ..................................6.99
• Fajita Asada & egg ......................................7.99
• Barbacoa Plate ............................................6.99
• ( add two eggs )............................................7.99
• **************GOURMET BREAKFAST*****
• Lurma's Favorite .............................................7.99
• two eggs , one slice of ham , two bacon , two sausage links and two buttermilk pancakes
• Lurma's Special ..........................................................3.99
• Two eggs , sausage , ham or bacon
• Ham and cheese Omelette .......................................6.99
• three egg omelette filled with ham and cheese , hash-brown and toast.
• Ultimate Omelette ....................................................7.99
• Three egg omelette with sausage , bacon , fire roasted bell peppers and onion , mushrooms , diced tomatoes and shredded cheese . served with hash-browns and toast .
• Meat lovers Omelette ......................................................8.99
• Three egg omelette with grilled steak , fire roasted bell peppers and onions.
• sauteed mushrooms and melted mozzarella cheese.
• The steakwich ...............................................7.99
• two scrambled eggs, tender steak , american cheese on texas toast .
• Hamwich .......................................................5.99
• sausagewich .................................................5.99
• Chicken Fried steak and eggs .......................7.99
• Pork chops and Eggs .....................................9.99
• T Bone Steak and eggs ...............................10.99
• **********BREAKFAST TACOS ********************
• Bacon & egg ...................1.99
• Sausage & Egg ................1.99
• Potato & Egg...................1.99
• Chorizo & Egg .................1.99
• Bean &Egg.......................1.99
• Ham and Egg ....................1.99
• Machacado & Egg ............2.59
• Chicharron & Egg .............2.59
• Gorditas .............................2.99
• *****extra taco filling *** .35
• *********DRINKS ***********
• Coffee..............................1.99
• Milk ..................................1.99
• Orange Juice ...................2.50
• (no refill )
• Sweet & unsweet Tea ..........2.15
• Raspberry Tea ...................2.50
• Fountain Drinks ..................2.15
• Strawberry lemonade ...........2.50
• Lemonade .............................2.50
• hot chocolate ...........................1.99
• *****15% WILL BE ADDED ON TABLES OF 6 OR MORE ***

```html
<!DOCTYPE html>
<html lang="en">
<head>
<meta charset="utf-8">
<title>Lurma's Menu</title>
<link href="https://fonts.googleapis.com/css2?family=Roboto+Condensed:wght@700&family=Arimo:ital@1&family=Open+Sans:ital,wght@0,400;1,700&display=swap" rel="stylesheet">
<style>
:root{
  --red:#c8161d;
  --orange:#f7941d;
  --green:#1d5e20;
  --ink:#111;
  --white:#fff;
}
*{margin:0;padding:0;box-sizing:border-box}
html,body{width:776px;height:1200px;overflow:hidden;background:var(--white)}
.menu{position:relative;width:776px;height:1200px;overflow:hidden;background:var(--white);font-family:"Roboto Condensed",sans-serif;color:var(--ink)}
.hero{position:absolute;left:0;top:0;width:776px;height:328px;overflow:hidden;border:4px solid var(--red);border-bottom:none}
.hero-photo{position:absolute;inset:0;background:
  radial-gradient(ellipse 110px 140px at 365px 150px,#eef0ea 0 60%,transparent 62%),
  linear-gradient(90deg,#e9dfb0 0,#e8d79a 38%,#b9612f 44%,#7a2410 62%,#9c3415 80%,#6a1e0d 100%)}
.diamond{position:absolute;width:34px;height:34px;transform:rotate(45deg);left:299px}
.d-red{background:var(--red)}.d-orange{background:var(--orange)}.d-green{background:var(--green)}
.brand-disc{position:absolute;left:516px;top:96px;width:288px;height:288px;border-radius:50%;background:var(--white);border:5px solid var(--orange)}
.brand-name{position:absolute;left:520px;top:216px;width:276px;text-align:center;font-size:44px;color:var(--orange);font-weight:700}
.frame-left-green{position:absolute;left:16px;top:328px;width:16px;height:872px;background:var(--green)}
.frame-left-orange{position:absolute;left:32px;top:328px;width:6px;height:840px;background:var(--orange)}
.frame-right-orange{position:absolute;left:736px;top:328px;width:8px;height:840px;background:var(--orange)}
.frame-right-green{position:absolute;left:744px;top:328px;width:16px;height:872px;background:var(--green)}
.frame-edge{position:absolute;left:0;top:328px;width:776px;height:872px;border:4px solid var(--red);border-top:none}
.frame-bottom-green{position:absolute;left:16px;top:1176px;width:744px;height:24px;background:var(--green)}
.frame-bottom-orange{position:absolute;left:38px;top:1166px;width:698px;height:6px;background:var(--orange)}
.dot{position:absolute;top:1158px;width:22px;height:22px;border-radius:50%;background:var(--red);border:2px solid var(--white)}
.column-box{position:absolute;top:392px;width:322px;height:672px;border:3px solid var(--orange)}
.heading{position:absolute;text-align:center;font-size:17px;letter-spacing:.2px}
.heading.ruled span{display:inline-block;border-bottom:3px solid var(--red);padding:0 4px 1px}
.subhead{position:absolute;text-align:center;font-family:"Arimo",sans-serif;font-style:italic;font-size:13px}
.item{position:absolute;display:flex;align-items:flex-end;font-size:13px;line-height:16px}
.item .leader{flex:1;border-bottom:2px dotted var(--ink);margin:0 2px 4px}
.note{position:absolute;font-family:"Arimo",sans-serif;font-style:italic;font-size:12.5px;line-height:16px}
.left-col{left:66px;width:300px}
.right-col{left:408px;width:299px}
.banner{position:absolute;left:94px;top:1076px;width:592px;height:60px;border-radius:14px;background:linear-gradient(90deg,var(--red),#d8381b 55%,var(--orange));color:var(--white);text-align:center;font-family:"Open Sans",sans-serif}
.banner-title{font-style:italic;font-weight:700;font-size:22px;line-height:28px;padding-top:4px}
.banner-text{font-size:15.5px;line-height:20px}
</style>
</head>
<body>
<main class="menu">
  <header class="hero">
    <div class="hero-photo" role="img" aria-label="Photo of shrimp penne pasta in cream sauce beside glazed chicken wings with ranch dip"></div>
    <div class="diamond d-red" style="top:11px"></div>
    <div class="diamond d-orange" style="top:63px"></div>
    <div class="diamond d-green" style="top:115px"></div>
    <div class="diamond d-red" style="top:171px"></div>
    <div class="diamond d-orange" style="top:223px"></div>
    <div class="diamond d-green" style="top:275px"></div>
    <div class="brand-disc"></div>
    <div class="brand-name">Lurma's</div>
  </header>

  <div class="frame-edge"></div>
  <div class="frame-left-green"></div>
  <div class="frame-left-orange"></div>
  <div class="frame-right-orange"></div>
  <div class="frame-right-green"></div>
  <div class="frame-bottom-orange"></div>
  <div class="frame-bottom-green"></div>
  <div class="dot" style="left:65px"></div>
  <div class="dot" style="left:689px"></div>

  <section class="column-box" style="left:54px"></section>
  <section class="column-box" style="left:398px"></section>

  <!-- Left column -->
  <h2 class="heading left-col" style="top:400px">PASTAS</h2>
  <div class="item left-col" style="top:434px"><span>Chicken Fettuccine or Penne Pasta</span><span class="leader"></span><span>9.25</span></div>
  <div class="item left-col" style="top:467px"><span>Shrimp Fettuccine or Penne Pasta</span><span class="leader"></span><span>10.25</span></div>

  <h2 class="heading ruled left-col" style="top:549px"><span>FROM THE BAR-B-QUE</span></h2>
  <p class="subhead left-col" style="top:579px">baby back ribs</p>
  <div class="item left-col" style="top:609px"><span>Half Rack</span><span class="leader"></span><span>12.99</span></div>
  <div class="item left-col" style="top:642px"><span>Full Rack</span><span class="leader"></span><span>18.99</span></div>
  <div class="item left-col" style="top:674px"><span>Brisket Burger</span><span class="leader"></span><span>8.25</span></div>
  <div class="item left-col" style="top:707px"><span>Barbecue Combo</span><span class="leader"></span><span>17.99</span></div>
  <p class="note left-col" style="top:724px">(half rack of ribs, brisket &amp; sausage served with potato salad and red beans).</p>

  <h2 class="heading ruled left-col" style="top:829px"><span>WINGS</span></h2>
  <p class="subhead left-col" style="top:856px">boneless or traditional</p>
  <div class="item left-col" style="top:888px"><span>5 Wings</span><span class="leader"></span><span>5.99</span></div>
  <div class="item left-col" style="top:921px"><span>10 Wings</span><span class="leader"></span><span>8.99</span></div>
  <div class="item left-col" style="top:954px"><span>20 Wings</span><span class="leader"></span><span>14.99</span></div>
  <div class="item left-col" style="top:987px"><span>50 Wings</span><span class="leader"></span><span>35.99</span></div>
  <p class="note left-col" style="top:1010px;text-align:center">mild, hot, lemon pepper, sweet chili<br>teriyaki, garlic parmesan</p>

  <!-- Right column -->
  <h2 class="heading right-col" style="top:400px">SPECIALTIES</h2>
  <div class="item right-col" style="top:436px"><span>Chile Relleno</span><span class="leader"></span><span>9.99</span></div>
  <p class="note right-col" style="top:453px">(ground beef or cheese )</p>
  <div class="item right-col" style="top:486px"><span>Shrimp &amp; Cheese Chile Relleno</span><span class="leader"></span><span>10.99</span></div>
  <div class="item right-col" style="top:518px"><span>Hamburger Steak</span><span class="leader"></span><span>8.99</span></div>
  <div class="item right-col" style="top:551px"><span>8 oz Grilled Chicken Breast</span><span class="leader"></span><span>8.99</span></div>
  <div class="item right-col" style="top:584px"><span>Chicken Fried Chicken</span><span class="leader"></span><span>8.99</span></div>
  <div class="item right-col" style="top:617px"><span>Chicken Fried Steak</span><span class="leader"></span><span>8.99</span></div>
  <div class="item right-col" style="top:650px"><span>T-Bone</span><span class="leader"></span><span>12.99</span></div>
  <div class="item right-col" style="top:683px"><span>Pork Chops</span><span class="leader"></span><span>8.99</span></div>
  <div class="item right-col" style="top:716px"><span>Arrachera Steak</span><span class="leader"></span><span>9.99</span></div>

  <h2 class="heading ruled right-col" style="top:769px"><span>COMBINATION PLATES</span></h2>
  <div class="item right-col" style="top:806px"><span>Lurma's Special</span><span class="leader"></span><span>8.99</span></div>
  <p class="note right-col" style="top:823px">(fajita with two enchiladas on the side, rice and beans )</p>
  <div class="item right-col" style="top:856px"><span>Tampiquena</span><span class="leader"></span><span>9.99</span></div>
  <p class="note right-col" style="top:873px">(fajita steak with two enchiladas on the side,<br>rice &amp; beans)</p>
  <div class="item right-col" style="top:922px"><span>Rio Bravo Plate</span><span class="leader"></span><span>11.99</span></div>
  <p class="note right-col" style="top:939px">(1 beef or cheese chile relleno with fajita steak<br>on the side, rice &amp; beans )</p>
  <div class="item right-col" style="top:988px"><span>Fajita &amp; Shrimp plate</span><span class="leader"></span><span>11.99</span></div>
  <div class="item right-col" style="top:1021px"><span>T-Bone &amp; Shrimp</span><span class="leader"></span><span>13.99</span></div>

  <aside class="banner">
    <p class="banner-title">Specialties</p>
    <p class="banner-text">South of Border, Combination Plates, Seafood, Soups, Family Platters.</p>
  </aside>
</main>
</body>
</html>
```